Menu for Traditional Persian Restraunt with Hookah - Name of Restaraunt is Venaro

We are a traditional Persian Restaraunt. We Provide Home Made Fresh Tradition Persian Meals Here in Sydney Australia
We also offer a Shisha Service in our back section of our Restaraunt.
The Restaurant Layout is like it is in IRAN, Very Unique nothing like it here in Australia. Day beds, persian Carpet, Timber Walls, Copper Lighting, Just to name a few. We want a menu that stands out and is very traditional in the Persian Way, but also is understandable for someone that isnt persian. Our Logo is a Sky Blue Colour ( which is a traditional well known colour in our country) Everything is Freshly made . We are open 7 days. Will Add Food Details andc Images in the next coming Days

Attached is our logo. I would want a space if possible to have an image of each food next to the decription. You can give me multiple option with or without, but some sort of images should be displayed even the footer and header of the menu.

I will be getting the menu printed as an A4 style book with leather front and back hard cover

I would like a SPEcial of the day Setion at the end of the menu with an emty page so i can put items on there.

Please give me ideas as i will be changing the items on special every few days

One of competitors is The Golden Ewer, Also if you have a quick look on google and type Tradition persian Food you will get an idea of the food and type of culture it is

Target Market(s)

All Cultures< Especially persians

Industry/Entity Type

It Service

Font styles to use
Sans Serif

Requirements
Must have
• Must have Blue colour Logo Provided
• Menu for Food
• Menu for Hookah
• Menu for Coffee
• Seperate Menu for Takeaway
Nice to have
• Traditional type theme in background like persian carpet( google search - hand made traditional carpet)
• needs to be easily read and undestandable

```html
<!DOCTYPE html>
<html lang="en">
<head>
<meta charset="UTF-8">
<title>Venaro — Kababs Menu</title>
<link rel="stylesheet" href="https://fonts.googleapis.com/css2?family=Open+Sans:ital,wght@0,400;0,600;0,700;1,400&family=Montserrat:wght@700;800&display=swap">
<style>
  :root {
    --page: #f6ece4;
    --page-deep: #ecdcd0;
    --teal: #1f8fa6;
    --orange: #e0892b;
    --leader: #9fbcc4;
    --photo-a: #b4552a;
    --photo-b: #7a3a1c;
    --plate-a: #f2d9a0;
    --plate-b: #8a4a22;
  }
  * { box-sizing: border-box; margin: 0; padding: 0; }
  html, body { width: 849px; height: 1200px; overflow: hidden; background: #fff; }
  .menu-page {
    position: relative;
    width: 849px;
    height: 1200px;
    overflow: hidden;
    background: radial-gradient(ellipse at 60% 55%, var(--page) 0%, var(--page-deep) 100%);
    font-family: "Open Sans", sans-serif;
  }
  .pattern-backdrop {
    position: absolute;
    inset: 250px 0 0 0;
    background: radial-gradient(circle at 70% 40%, rgba(210,185,170,0.35) 0%, rgba(210,185,170,0) 60%);
  }
  .hero-photo {
    position: absolute;
    left: 0; top: 0;
    width: 849px; height: 255px;
    background: linear-gradient(160deg, var(--photo-a) 0%, #c9683a 45%, var(--photo-b) 100%);
    border-bottom-left-radius: 40px 20px;
    border-bottom-right-radius: 40px 20px;
  }
  .section-title {
    position: absolute;
    left: 62px; top: 322px;
    display: flex; align-items: center; gap: 14px;
    font-family: "Montserrat", sans-serif;
    font-weight: 800;
    font-size: 38px;
    letter-spacing: 1px;
    color: var(--teal);
  }
  .dish-list {
    position: absolute;
    left: 80px; top: 398px;
    width: 690px;
    list-style: none;
  }
  .dish {
    display: flex;
    align-items: flex-start;
    height: 96px;
  }
  .dish-photo {
    flex: none;
    width: 112px; height: 68px;
    border-radius: 50%;
    background: radial-gradient(ellipse at 50% 50%, var(--plate-b) 0%, #b0703a 35%, var(--plate-a) 60%, #fff7e6 75%);
    border: 3px solid #e8b84a;
    margin-right: 40px;
    margin-top: 4px;
  }
  .dish-body { flex: 1; }
  .dish-head {
    display: flex; align-items: baseline;
    font-weight: 600;
    font-size: 19px;
    color: var(--teal);
  }
  .dish-leader {
    flex: 1;
    margin: 0 8px;
    border-bottom: 2px dotted var(--leader);
    transform: translateY(-5px);
  }
  .dish-desc {
    margin-top: 6px;
    font-style: italic;
    font-size: 13.5px;
    line-height: 1.35;
    color: var(--orange);
  }
  .brand-mark {
    position: absolute;
    left: 0; right: 0; top: 1108px;
    display: flex; justify-content: center; align-items: center; gap: 8px;
    font-weight: 700;
    font-size: 20px;
    color: var(--teal);
  }
  .brand-dot { width: 12px; height: 12px; border-radius: 50%; background: var(--teal); }
</style>
</head>
<body>
<main class="menu-page">
  <div class="pattern-backdrop" role="img" aria-label="Faint Persian carpet mandala pattern"></div>
  <div class="hero-photo" role="img" aria-label="Photo of grilled chicken kabab skewers with a lime wedge"></div>

  <h1 class="section-title">KABABS
    <svg width="30" height="18" viewBox="0 0 30 18" aria-hidden="true">
      <circle cx="18" cy="9" r="5" fill="none" stroke="#1f8fa6" stroke-width="2"/>
      <line x1="0" y1="9" x2="12" y2="9" stroke="#1f8fa6" stroke-width="2"/>
      <line x1="24" y1="9" x2="30" y2="9" stroke="#1f8fa6" stroke-width="2"/>
    </svg>
  </h1>

  <ul class="dish-list">
    <li class="dish"><div class="dish-photo" role="img" aria-label="Plate of chelo kabab with rice"></div><div class="dish-body"><div class="dish-head"><span>Chelo Kabab Soltani</span><span class="dish-leader"></span><span>10.99$</span></div><p class="dish-desc">Gosht Barre, Goje, Felfel, There are many variations of passages of Lorem Ipsum avail-able.</p></div></li>
    <li class="dish"><div class="dish-photo" role="img" aria-label="Plate of chelo kabab with rice"></div><div class="dish-body"><div class="dish-head"><span>Chelo Kabab Soltani</span><span class="dish-leader"></span><span>10.99$</span></div><p class="dish-desc">Gosht Barre, Goje, Felfel, There are many variations of passages of Lorem Ipsum avail-able.</p></div></li>
    <li class="dish"><div class="dish-photo" role="img" aria-label="Plate of chelo kabab with rice"></div><div class="dish-body"><div class="dish-head"><span>Chelo Kabab Soltani</span><span class="dish-leader"></span><span>10.99$</span></div><p class="dish-desc">Gosht Barre, Goje, Felfel, There are many variations of passages of Lorem Ipsum avail-able.</p></div></li>
    <li class="dish"><div class="dish-photo" role="img" aria-label="Plate of chelo kabab with rice"></div><div class="dish-body"><div class="dish-head"><span>Chelo Kabab Soltani</span><span class="dish-leader"></span><span>10.99$</span></div><p class="dish-desc">Gosht Barre, Goje, Felfel, There are many variations of passages of Lorem Ipsum avail-able.</p></div></li>
    <li class="dish"><div class="dish-photo" role="img" aria-label="Plate of chelo kabab with rice"></div><div class="dish-body"><div class="dish-head"><span>Chelo Kabab Soltani</span><span class="dish-leader"></span><span>10.99$</span></div><p class="dish-desc">Gosht Barre, Goje, Felfel, There are many variations of passages of Lorem Ipsum avail-able.</p></div></li>
    <li class="dish"><div class="dish-photo" role="img" aria-label="Plate of chelo kabab with rice"></div><div class="dish-body"><div class="dish-head"><span>Chelo Kabab Soltani</span><span class="dish-leader"></span><span>10.99$</span></div><p class="dish-desc">Gosht Barre, Goje, Felfel, There are many variations of passages of Lorem Ipsum avail-able.</p></div></li>
    <li class="dish"><div class="dish-photo" role="img" aria-label="Plate of chelo kabab with rice"></div><div class="dish-body"><div class="dish-head"><span>Chelo Kabab Soltani</span><span class="dish-leader"></span><span>10.99$</span></div><p class="dish-desc">Gosht Barre, Goje, Felfel, There are many variations of passages of Lorem Ipsum avail-able.</p></div></li>
  </ul>

  <footer class="brand-mark"><span class="brand-dot"></span><span>Venaro</span></footer>
</main>
</body>
</html>
```